Poster Design

Hello,

My name is Rowan Pickett and I run a vidora channel called 'CrumbleDiary'. I want a poster made for those who watch my video to purchase and put on their wall at home. The poster will be all text and as you can see, I've attached a few examples of posters which I would like it to be similar to. I use a lot of the colour #ab6f7f so it would be good to incorporate this in somewhere (maybe the background colour).
I would like the poster to say:
"Do More Of What Makes YOU Happy"
I need this poster to be for sale ready for christmas, so Im going to need the designs created as soon as possible. Im sorry for the rush.
Have fun with it and feel free to upload multiple versions of a design as well as a few designs if you like.
I look forward to seeing what you come up with.
Rowan
(Of course I will need to own all rights once the payment has been made)

```html
<!DOCTYPE html>
<html lang="en">
<head>
<meta charset="utf-8">
<title>Do More of What Makes You Happy — Poster</title>
<link rel="stylesheet" href="https://fonts.googleapis.com/css2?family=Abril+Fatface&family=Pinyon+Script&family=Quicksand:wght@300;400&display=swap">
<style>
  :root {
    --ink-navy: #06405f;
    --paper-white: #ffffff;
    --accent-orange: #f26b22;
    --accent-yellow: #f5d31c;
    --accent-mint: #8fdcc6;
    --accent-rose: #ab6f7f;
  }
  * { margin: 0; padding: 0; box-sizing: border-box; }
  html, body { width: 900px; height: 1200px; overflow: hidden; background: var(--ink-navy); }
  .poster {
    position: relative;
    width: 900px;
    height: 1200px;
    background: var(--ink-navy);
    overflow: hidden;
    color: var(--paper-white);
  }
  .headline {
    position: absolute;
    left: 0; top: 34px;
    width: 900px;
    text-align: center;
    font-family: "Abril Fatface", "Georgia", serif;
    font-weight: 400;
    font-size: 196px;
    line-height: 1;
    letter-spacing: 0;
    color: var(--paper-white);
    text-shadow:
      -4px 5px 0 var(--ink-navy),
      -7px 8px 0 var(--accent-orange),
      -9px 11px 0 var(--accent-orange),
      -11px 13px 0 var(--accent-orange);
  }
  .of-divider { position: absolute; left: 0; top: 285px; width: 900px; height: 110px; }
  .of-word {
    font-family: "Pinyon Script", cursive;
    font-size: 72px;
    fill: var(--paper-white);
  }
  .subline {
    position: absolute;
    left: 0; top: 368px;
    width: 900px;
    text-align: center;
    font-family: "Quicksand", "Helvetica", sans-serif;
    font-weight: 400;
    font-size: 136px;
    line-height: 1;
    letter-spacing: 1px;
  }
  .rule-pair { position: absolute; left: 25px; width: 850px; height: 16px; }
  .rule-pair::before, .rule-pair::after {
    content: ""; position: absolute; left: 0; width: 100%; background: var(--paper-white);
  }
  .rule-pair::before { top: 0; height: 5px; }
  .rule-pair::after { top: 11px; height: 3px; }
  .rule-top { top: 510px; }
  .rule-bottom { top: 910px; }
  .focus-word { position: absolute; left: 0; top: 530px; width: 900px; height: 370px; }
  .focus-word text {
    font-family: "Quicksand", "Helvetica", sans-serif;
    font-weight: 400;
    font-size: 392px;
  }
  .closing {
    position: absolute;
    left: 0; top: 930px;
    width: 900px;
    text-align: center;
    font-family: "Quicksand", "Helvetica", sans-serif;
    font-weight: 300;
    font-size: 214px;
    line-height: 1;
  }
  .closing-word {
    display: inline-block;
    transform: scaleX(0.82);
    transform-origin: center;
  }
  .flourish {
    position: absolute;
    top: 1000px;
    width: 112px;
    height: 76px;
    border-radius: 38px;
    background: var(--accent-yellow);
  }
  .flourish-left { left: 54px; }
  .flourish-right { left: 736px; }
</style>
</head>
<body>
<main class="poster">
  <h1 class="headline">Do More</h1>

  <svg class="of-divider" viewBox="0 0 900 110">
    <line x1="52" y1="57" x2="378" y2="57" stroke="var(--accent-yellow)" stroke-width="12" stroke-dasharray="3 3"/>
    <line x1="522" y1="57" x2="846" y2="57" stroke="var(--accent-yellow)" stroke-width="12" stroke-dasharray="3 3"/>
    <circle cx="450" cy="55" r="48" fill="none" stroke="var(--accent-mint)" stroke-width="5"/>
    <text class="of-word" x="450" y="80" text-anchor="middle">of</text>
  </svg>

  <p class="subline">what makes</p>

  <div class="rule-pair rule-top"></div>

  <svg class="focus-word" viewBox="0 0 900 370">
    <g>
      <text x="60" y="310" textLength="780" lengthAdjust="spacingAndGlyphs" transform="translate(14 22)"><tspan fill="var(--accent-yellow)">Y</tspan><tspan fill="var(--accent-rose)">O</tspan><tspan fill="var(--accent-yellow)">U</tspan></text>
      <text x="60" y="310" textLength="780" lengthAdjust="spacingAndGlyphs" transform="translate(7 11)"><tspan fill="var(--accent-yellow)">Y</tspan><tspan fill="var(--accent-rose)">O</tspan><tspan fill="var(--accent-yellow)">U</tspan></text>
      <text x="60" y="310" textLength="780" lengthAdjust="spacingAndGlyphs" fill="var(--paper-white)">YOU</text>
    </g>
  </svg>

  <div class="rule-pair rule-bottom"></div>

  <div class="flourish flourish-left" role="img" aria-label="Yellow scroll flourish"></div>
  <p class="closing"><span class="closing-word">HAPPY</span></p>
  <div class="flourish flourish-right" role="img" aria-label="Yellow scroll flourish"></div>
</main>
</body>
</html>
```